Etiketten für Nahrungsergänzungsmittel
Zielgruppe
Wir stellen Nahrungsergänzungen her für psychische Gesundheit. Zielgruppe: jüngere Menschen 20-40 Jahre alt mit Interesse an Naturheilkunde. Firmenname: Velmora Works. Logo der Firma: s. Anhang
Aufgabenstellung
Dosenetikett 155 x 50 mm, für Kapseln mit Pflanzenextrakten aus Korallenbaum. Für besseren Schlaf und zur Beruhigung. Produktname: Sternkiesel

```html
<!DOCTYPE html>
<html lang="de">
<head>
<meta charset="utf-8">
<title>Sternkiesel – Dosenetikett</title>
<link rel="stylesheet" href="https://fonts.googleapis.com/css2?family=Roboto:wght@300;400;500&display=swap">
<style>
  :root {
    --backdrop: #cfcfcf;
    --label: #ffffff;
    --ink: #2b2b2b;
    --ink-soft: #555555;
    --ink-faint: #9a9a9a;
    --product-red: #b8262a;
    --petal-red: #d9453c;
    --petal-light: #ee8a7c;
    --oval-blush: #f4dcd4;
    --oval-sage: #dfe9cf;
    --frame: #4a4a4a;
  }
  * { box-sizing: border-box; margin: 0; padding: 0; }
  html, body {
    width: 1200px; height: 849px; overflow: hidden;
    background: var(--backdrop);
    font-family: "Roboto", Arial, sans-serif;
    font-weight: 300;
    color: var(--ink);
  }
  .can-label {
    position: absolute; left: 40px; top: 244px;
    width: 1120px; height: 361px;
    background: var(--label);
    overflow: hidden;
  }
  .legal-info {
    position: absolute; left: 18px; top: 20px; width: 330px;
    font-size: 14px; line-height: 18.3px; color: var(--ink-soft);
    white-space: nowrap;
  }
  .legal-info p + p { margin-top: 18px; }
  .legal-info strong { font-weight: 400; color: var(--ink); }

  .flower-art { position: absolute; z-index: 1; }
  .flower-art--top {
    left: 592px; top: -10px; width: 172px; height: 165px;
    background: radial-gradient(ellipse at 55% 40%, var(--petal-red) 0%, var(--petal-light) 65%, rgba(238,138,124,0) 100%);
    border-radius: 45% 55% 50% 50%;
  }
  .flower-art--bottom {
    left: 318px; top: 190px; width: 118px; height: 171px;
    background: radial-gradient(ellipse at 50% 45%, var(--petal-red) 0%, var(--petal-light) 60%, rgba(238,138,124,0) 100%);
    border-radius: 50% 50% 40% 60%;
  }

  .claim-oval {
    position: absolute; z-index: 2;
    left: 392px; top: 226px; width: 370px; height: 122px;
    border-radius: 50%;
    background: var(--oval-blush);
    box-shadow: 8px -4px 0 6px var(--oval-sage);
  }

  .brand {
    position: absolute; z-index: 3; left: 460px; top: 24px; width: 200px;
    text-align: center;
  }
  .brand-dot {
    display: block; width: 64px; height: 64px; margin: 0 auto 8px;
    border-radius: 50%; background: var(--ink);
  }
  .brand-name { font-size: 14px; font-weight: 500; color: var(--ink); }

  .product-name {
    position: absolute; z-index: 3; left: 420px; top: 150px; width: 280px;
    text-align: center;
    font-size: 40px; font-weight: 300; letter-spacing: 0;
    color: var(--product-red);
  }
  .claim {
    position: absolute; z-index: 3; left: 380px; top: 268px; width: 400px;
    text-align: center;
    font-size: 13.5px; line-height: 18.5px; color: var(--ink-soft);
  }
  .claim strong { font-weight: 400; color: var(--ink); }

  .nutrition-box {
    position: absolute; z-index: 3; left: 774px; top: 24px; width: 320px; height: 246px;
    background: var(--label);
    border: 1px solid var(--frame);
    padding: 4px 6px 0 10px;
    text-align: right;
    font-size: 14px; line-height: 18.2px; color: var(--ink-soft);
    white-space: nowrap;
  }
  .nutrition-box p + p { margin-top: 18px; }

  .best-before {
    position: absolute; left: 905px; top: 296px; width: 189px; height: 44px;
    border: 1px solid var(--frame);
    padding: 7px 3px;
    font-size: 12px; line-height: 15px; color: var(--ink);
    white-space: nowrap;
  }
  .best-before span { color: var(--ink-faint); }
</style>
</head>
<body>
  <main class="can-label">
    <section class="legal-info">
      <p>Zutaten: Mulunguextrakt</p>
      <p>Nahrungsergänzungsmittel –<br>sollte nicht als Ersatz für eine ausgewogene<br>und abwechslungsreiche Ernährung<br>verwendet werden. Außerhalb der Reichweite<br>kleiner Kinder aufbewahren.<br>Kühl und trocken lagern.</p>
      <p>Hergestellt in Deutschland.<br><strong>Velmora Works GmbH</strong>, Lindenhofer Str. 42B<br>D-37085 Göttingen<br>www.velmora-works.de</p>
    </section>

    <div class="flower-art flower-art--top" role="img" aria-label="Aquarell-Illustration roter Korallenbaumblüten mit grünem Zweig"></div>
    <div class="flower-art flower-art--bottom" role="img" aria-label="Aquarell-Illustration einer roten Korallenbaumblüte mit grünen Blättern"></div>
    <div class="claim-oval"></div>

    <div class="brand">
      <span class="brand-dot"></span>
      <span class="brand-name">Velmora Works</span>
    </div>

    <h1 class="product-name">STERNKIESEL</h1>

    <p class="claim">90 KAPSELN À 500 MG EXTRAKT<br>AUS DER <strong>KORALLENBAUMWURZEL</strong><br>FÜR BESSEREN SCHLAF UND ZUR BERUHIGUNG</p>

    <section class="nutrition-box">
      <p>Zutatenliste:<br>Gemahlener Extrakt aus Korallenbaumwurzel,<br>Cellulose-Kapsel</p>
      <p>Empfohlene Tagesverzehrmenge:<br>pro 100G 100G Mulungu<br>pro 100G 10mg Erythravin</p>
      <p>Verzehrempfehlung:<br>Ein- bis Zweimal täglich je eine Kapsel<br>zu den Mahlzeiten einnehmen.<br>Tägliche Verzehrmenge<br>nicht überschreiten.</p>
    </section>

    <div class="best-before">mindestens haltbar<br>bis Ende: <span>XX/XXXX Lot-Nr.XXXXX</span></div>
  </main>
</body>
</html>
```